Business Card design for leader Solar Energy company
Loreno Energy Group
Professional
Belisa Torv
CEO
Santo Domingo: Calle Olmeda Vieja #418, Edif. Torv Corporativo, Suite 512
Las Terrenas: Calle de las Brisas, Coral Vista Plaza, Suite 512
Punta Cana; Proximamente
809.741.LORE (5673)
belisa@lorenopower-example.com
www.lorenopower-example.com
Think Green, Save Money, Go Solar.
Please use this logo for the business card design.
Thank you,
-belisa
vector logo

```html
<!DOCTYPE html>
<html lang="en">
<head>
<meta charset="utf-8">
<title>Loreno Energy Group — Business Card</title>
<link href="https://fonts.googleapis.com/css2?family=Open+Sans:wght@400;600;700&display=swap" rel="stylesheet">
<style>
  :root {
    --stage: #ecebe8;
    --card: #ffffff;
    --brand-blue: #1d5b97;
    --brand-green: #3c8a3e;
    --text: #4a4a4a;
    --rule: #c9d3de;
  }
  * { margin: 0; padding: 0; box-sizing: border-box; }
  html, body {
    width: 1200px; height: 413px; overflow: hidden;
    background: var(--stage);
    font-family: "Open Sans", Arial, sans-serif;
  }
  .card {
    position: absolute; top: 79px;
    width: 532px; height: 270px;
    background: var(--card);
    box-shadow: 0 3px 8px rgba(0,0,0,0.25);
  }
  .card--front { left: 52px; }
  .card--back { left: 614px; }

  .wordmark {
    display: flex; align-items: center; gap: 10px;
    color: var(--brand-blue); font-weight: 600;
  }
  .wordmark__dot {
    border-radius: 50%; background: var(--brand-green); flex: none;
  }
  .card--front .wordmark {
    position: absolute; left: 28px; top: 112px;
    font-size: 17px; letter-spacing: 0.5px; width: 230px;
  }
  .card--front .wordmark__dot { width: 14px; height: 14px; }

  .divider {
    position: absolute; left: 258px; top: 28px; bottom: 28px;
    width: 1px; background: var(--rule);
  }
  .details {
    position: absolute; left: 276px; top: 28px; right: 16px;
    color: var(--text); font-size: 11px; line-height: 15px;
  }
  .details__name { color: var(--brand-blue); font-weight: 700; font-size: 15px; }
  .details__role { color: var(--text); font-weight: 400; font-size: 11px; }
  .contact { list-style: none; margin-top: 22px; }
  .contact li { display: flex; align-items: center; gap: 5px; }
  .contact svg { width: 9px; height: 9px; fill: var(--text); flex: none; }
  .address { margin-top: 10px; }
  .address + .address { margin-top: 8px; }

  .card--back .wordmark {
    position: absolute; left: 0; right: 0; top: 96px;
    justify-content: center; font-size: 34px; letter-spacing: 1px;
  }
  .card--back .wordmark__dot { width: 26px; height: 26px; }
  .tagline {
    position: absolute; left: 0; right: 0; top: 192px;
    text-align: center; color: var(--text); font-size: 15px;
  }
</style>
</head>
<body>
  <section class="card card--front">
    <div class="wordmark"><span class="wordmark__dot"></span>Loreno Energy Group</div>
    <div class="divider"></div>
    <div class="details">
      <p><span class="details__name">Belisa Torv</span> <span class="details__role">/ CEO</span></p>
      <ul class="contact">
        <li><svg viewBox="0 0 10 10"><path d="M2 0h2l1 3-1.5 1a6 6 0 0 0 2.5 2.5L7 5l3 1v2a2 2 0 0 1-2 2A8 8 0 0 1 0 2a2 2 0 0 1 2-2z"/></svg>809.741.LORE (5673)</li>
        <li><svg viewBox="0 0 10 10"><rect x="2.5" y="0" width="5" height="10" rx="1"/></svg>829.620.3187</li>
        <li><svg viewBox="0 0 10 10"><path d="M0 2h10v6H0z M0 2l5 3 5-3" /></svg>belisa@lorenopower-example.com</li>
        <li><svg viewBox="0 0 10 10"><circle cx="5" cy="5" r="5"/></svg>www.lorenopower-example.com</li>
      </ul>
      <p class="address">Santo Domingo: Calle Olmeda Vieja #418<br>Edif. Torv Corporativo, Suite 512</p>
      <p class="address">Las Terrenas: Calle de las Brisas<br>Coral Vista Plaza, Suite 512<br>Punta Cana; Proximamente</p>
    </div>
  </section>

  <section class="card card--back">
    <div class="wordmark"><span class="wordmark__dot"></span>Loreno Energy Group</div>
    <p class="tagline">Think Green, Save Money, Go Solar.</p>
  </section>
</body>
</html>
```